Pruett Design & Millwork needs a web presence. Looking for a unique Design so please submit an idea.

In brief, you should know the following about me: My company was established in 2001 and had been responsible for providing reasonable CAD Design and Custom Millwork ever since. My specialty is in the area Architectural CAD Design, Fabrication of Custom Millwork and Mouldings on a partime basis. Drawings and estimates done at a very reasonable cost. I look forward to working on your next project. Thanks in Advance, Glen 
I would like one page to show thumbnails linked to some of past millwork projects and another page with thumbnails linking to some of my house designs. I assume last page will have contact information accessed from a link on home page. I already had a logo designed which I can supply you with to design home page around. As I indicated I have a regular full time job and do this for additional income and will move to full time when I have enough business.

I have attached the logo I had designed in a couple different colors. I have also uploaded some PDF's of files that I also considered before choosing the RED LOGO to give an ideas of how we could tweak the logo to better fit the website if need be. Text is wrong in those.

Thanks,
Glen

I added my logo as a PDF side there seems to be a problem with scaling loge with the other file. Hope this helps.

Glen

Evening,
I will be hosting this site on servquill. Its looks like it will get launched with wordpress?  What will be involved from getting your design up so I can upload project pictures and and text to areas you have set aside? I am also going to upload a couple jpg of a couple recent projects so you can put in so I can get a feel of what they will look like. Thanks for all your work to date! Glen

I am not seeing alot of design variations or even many designers in fact. Is there something more from me you need? Do you need me to extend deadline?

Reason: It appears that your need some more time to submit some design changes. I will choose a design next week after changes have been submitted. Thanks for your time. Glen

Reason: Designers needs a couple days to submit some last minute changes. Thanks for all your submissions! Glen

Reason: Some last minute designs that I need to look at and give feedback on. I want to thank everyone for their designs and patience. Thanks again, Glen

Evening All,

Upon discussion with a couple of the designers I want the design done in Word Press and I have increased budget the amount they said they would need to do it for. Thanks for all submissions so far but I am still looking for the special one that stands out among the rest! Glen

I will not be extending deadline and choosing designer tomorrow morning so if you have anything else to add please do so tonight. Thanks for all your submissions. Glen

Target Market(s)

Millwork projects will be generally local where as CAD Design Projects could be emailed anywhere. Probably more USA but who knows.

Industry/Entity Type

House

Font styles to use
Other font styles liked:
• Eras Medium ITC, Calibri or Designers choice.

Requirements
Must have
• Must tie in my logo on Homepage at least. Could even be somewhat transparent in background? I will let the designer work that out.
Nice to have
• Page to point to current and past Design projects on one page and millwork on another.
Should not have
• Target a large Corporate or Global environment since it is a small business right now.

```html
<!DOCTYPE html>
<html lang="en">
<head>
<meta charset="utf-8">
<title>Contact Us – Pruett Design &amp; Millwork</title>
<link rel="stylesheet" href="https://fonts.googleapis.com/css2?family=Open+Sans:wght@300;400;600;700&display=swap">
<style>
:root{
  --brand-red:#9b1c1c;
  --brand-red-dark:#6e0f10;
  --brand-red-light:#b02a2e;
  --text-dark:#2b2b2b;
  --text-body:#3a3a3a;
  --text-muted:#6a6a6a;
  --rule:#d9d9d9;
  --field-top:#fbfbfb;
  --field-bottom:#ececec;
  --field-border:#cfcfcf;
  --footer-bg:#3b3b3d;
  --footer-text:#e6e6e6;
  --footer-muted:#8e8e8e;
  --page-bg:#ffffff;
}
*{box-sizing:border-box;margin:0;padding:0}
html,body{width:1100px;height:1200px;overflow:hidden;background:var(--page-bg)}
body{position:relative;font-family:"Open Sans",Arial,sans-serif;color:var(--text-body)}

/* Header */
.site-header{position:absolute;left:0;top:0;width:1100px;height:148px;background:#fff;border-bottom:1px solid #e2e2e2;box-shadow:0 2px 4px rgba(0,0,0,.06)}
.brand{position:absolute;left:70px;top:40px;display:flex;align-items:center;gap:10px}
.brand-mark{width:22px;height:22px;background:var(--brand-red)}
.brand-name{font-size:19px;font-weight:600;color:var(--brand-red);line-height:1.15;width:130px}
.call-us{position:absolute;right:84px;top:34px;text-align:right}
.call-us-label{font-size:15px;font-weight:400;color:#555;letter-spacing:.2px}
.call-us-number{font-size:26px;font-weight:400;color:var(--brand-red);line-height:1.1;margin-top:2px}
.main-nav{position:absolute;right:84px;top:101px;display:flex;align-items:center}
.main-nav a{font-size:16.5px;font-weight:600;color:#222;text-decoration:none;text-transform:uppercase;padding:0 18px;border-left:1px solid #bdbdbd;line-height:18px}
.main-nav a:first-child{border-left:none}
.main-nav a:last-child{padding-right:0}
.main-nav a.is-current{color:var(--brand-red)}

/* Hero */
.hero{position:absolute;left:0;top:149px;width:1100px;height:248px;background:linear-gradient(90deg,#e9e9e9 0%,#d9b8a4 18%,#e0c4b2 35%,#f0f0f0 55%,#e4e4e4 80%,#efefef 100%);border-bottom:1px solid #dcdcdc}

/* Contact */
.page-title{position:absolute;left:74px;top:426px;font-size:30px;font-weight:400;color:var(--text-dark)}
.map-area{position:absolute;left:75px;top:471px;width:209px;height:146px;background:linear-gradient(135deg,#d9d6c6 0%,#9ec157 40%,#e8e2c4 60%,#6aa84f 85%,#5a9bd0 100%)}
.contact-info{position:absolute;left:300px;top:467px;width:520px}
.contact-intro{font-size:12.5px;font-weight:400;color:var(--text-muted);line-height:20.5px;text-align:justify}
.company-name{font-size:16px;font-weight:600;color:var(--text-dark);margin-top:9px}
.address{font-style:normal;font-size:13.5px;line-height:20.5px;color:var(--text-body);margin-top:1px}

/* Quote form */
.quote-panel{position:absolute;left:74px;top:657px;width:573px;height:350px;border:1px solid var(--rule);border-radius:4px;background:#fff;overflow:hidden}
.quote-panel-head{height:52px;background:linear-gradient(180deg,var(--brand-red-light) 0%,var(--brand-red) 55%,var(--brand-red-dark) 100%);padding-left:26px}
.quote-panel-head h2{font-size:22px;font-weight:400;color:#fff;line-height:52px}
.field{position:absolute;background:linear-gradient(180deg,var(--field-top),var(--field-bottom));border:1px solid var(--field-border);border-radius:2px;font-size:12.5px;color:#666;padding-left:11px;display:flex;align-items:center}
.field-name{left:28px;top:74px;width:242px;height:32px}
.field-email{left:281px;top:74px;width:242px;height:32px}
.field-phone{left:28px;top:120px;width:242px;height:32px}
.field-city{left:281px;top:120px;width:242px;height:32px}
.field-message{left:29px;top:166px;width:494px;height:112px;align-items:flex-start;padding-top:11px;padding-left:13px}
.submit-btn{position:absolute;left:28px;top:292px;width:116px;height:34px;border-radius:3px;background:linear-gradient(180deg,var(--brand-red-light),var(--brand-red-dark));box-shadow:0 1px 2px rgba(0,0,0,.35);color:#fff;font-size:15px;font-weight:700;display:flex;align-items:center;justify-content:center;letter-spacing:.2px}

/* Footer */
.site-footer{position:absolute;left:0;top:1069px;width:1100px;height:131px;background:var(--footer-bg);border-top:6px solid #dcdcdc}
.footer-brand{position:absolute;left:72px;top:30px;display:flex;align-items:center;gap:8px}
.footer-brand .brand-mark{width:16px;height:16px;background:#fff}
.footer-brand .brand-name{font-size:14px;color:#fff;width:80px}
.footer-nav{position:absolute;left:195px;top:34px;display:flex}
.footer-nav a{font-size:14.5px;color:var(--footer-text);text-decoration:none;padding:0 10px;border-left:1px solid #bbb;line-height:15px}
.footer-nav a:first-child{padding-left:0;border-left:none}
.copyright{position:absolute;left:195px;top:63px;font-size:12.5px;font-weight:300;color:var(--footer-muted)}
.social{position:absolute;right:81px;top:38px;display:flex;gap:8px}
.social span{width:23px;height:23px;border-radius:3px;display:block}
.social .s1{background:#3b5998}
.social .s2{background:#3fa9e0}
.social .s3{background:#1a78b4}
.social .s4{background:#f28a1b}
</style>
</head>
<body>

<header class="site-header">
  <div class="brand">
    <span class="brand-mark"></span>
    <span class="brand-name">Pruett Design &amp; Millwork</span>
  </div>
  <div class="call-us">
    <div class="call-us-label">CALL US NOW</div>
    <div class="call-us-number">623-555-0147</div>
  </div>
  <nav class="main-nav">
    <a href="#">Home</a>
    <a href="#">About us</a>
    <a href="#">Millwork projects</a>
    <a href="#">House designs</a>
    <a href="#" class="is-current">Contact us</a>
  </nav>
</header>

<div class="hero" role="img" aria-label="Photo of a smiling customer service agent wearing a headset"></div>

<h1 class="page-title">Contact Us</h1>
<div class="map-area" role="img" aria-label="Street map showing the office location"></div>

<section class="contact-info">
  <p class="contact-intro">Sed porta Suspendisse quam leo molestie sed luctus quis feugiat in pede Fusce tellus Sed metus augue convallis et vehicula ut pulvinar eu ante Integer orci tellus tristique</p>
  <h3 class="company-name">Glen Pruett Design &amp; Millwork</h3>
  <address class="address">
    48 Linden Avenue #4B<br>
    Riverton 10231 NY<br>
    Phoneno: (212) 555-0193<br>
    Email add:&nbsp; info@pruettmillwork.co.uk
  </address>
</section>

<section class="quote-panel">
  <div class="quote-panel-head"><h2>Request a Quote</h2></div>
  <div class="field field-name">Your Name</div>
  <div class="field field-email">Email address</div>
  <div class="field field-phone">Phone no.</div>
  <div class="field field-city">City/Location</div>
  <div class="field field-message">Message/Comments</div>
  <div class="submit-btn">SUBMIT</div>
</section>

<footer class="site-footer">
  <div class="footer-brand">
    <span class="brand-mark"></span>
    <span class="brand-name">Pruett Design &amp; Millwork</span>
  </div>
  <nav class="footer-nav">
    <a href="#">Home</a>
    <a href="#">About us</a>
    <a href="#">Millwork projects</a>
    <a href="#">House designs</a>
    <a href="#">Contact us</a>
  </nav>
  <div class="copyright">Copyright © 2013 Company Name.&nbsp; All right reserved</div>
  <div class="social" aria-label="Social links">
    <span class="s1"></span><span class="s2"></span><span class="s3"></span><span class="s4"></span>
  </div>
</footer>

</body>
</html>
```